Wayline Billboard Co Business Card Design

We have a newly created business and logo, but we now need business cards using the new logo.
We are an Australian based business, and we sell advertising space on trucks. The business cards will be seen by media buyers, direct advertisers, fleet owners and business people in general.
Our colours are very simple - black and a strong yellow, with some white. We have chosen the black and yellow for various reasons, but in particular because they are high contrast, and they also have a parallel with the number plates used on our roads, which is relevant to our product offering.
My initial thoughts:
Keep it simple and uncluttered
Use both sides
Our default is Century Gothic
I can provide logo files as required. We do not yet have a website, so I can't direct you there just yet. That may well be another project!
Target Market(s)
The business cards will be seen by media buyers, direct advertisers, fleet owners and business people in general.
Industry/Entity Type
Advertising
Look and feel
Each slider illustrates characteristics of the customer's brand and the style your logo design should communicate.

```html
<!DOCTYPE html>
<html lang="en">
<head>
<meta charset="utf-8">
<title>Wayline Billboard Co – Business Card</title>
<link rel="stylesheet" href="https://fonts.googleapis.com/css2?family=Questrial&family=Didact+Gothic&display=swap">
<style>
  :root {
    --yellow: #f3ec1f;
    --black: #1c1c1c;
    --charcoal: #3a3a3c;
    --grey-band: #5b5b5e;
    --ink: #3b3b3d;
    --backdrop: #e9e7e4;
  }
  * { box-sizing: border-box; margin: 0; padding: 0; }
  html, body { width: 1200px; height: 900px; overflow: hidden; }
  body {
    background: var(--backdrop);
    font-family: "Questrial", "Didact Gothic", sans-serif;
    position: relative;
  }
  .card {
    position: absolute;
    left: 300px;
    width: 600px;
    height: 360px;
    overflow: hidden;
    box-shadow: 0 4px 14px rgba(0,0,0,0.18);
  }
  /* Front */
  .card-front { top: 70px; background: var(--yellow); color: var(--ink); }
  .front-brand {
    position: absolute; left: 34px; top: 34px;
    display: flex; align-items: center; gap: 10px;
    font-size: 24px; color: var(--black); letter-spacing: 0.5px;
  }
  .brand-square { width: 16px; height: 16px; background: var(--black); }
  .divider {
    position: absolute; left: 0; right: 0; top: 124px;
    border-top: 1px solid var(--ink);
  }
  .company-block { position: absolute; left: 34px; top: 146px; font-size: 12px; line-height: 1.45; }
  .company-name { font-weight: 700; text-transform: uppercase; letter-spacing: 0.4px; }
  .person-block { position: absolute; right: 34px; top: 148px; width: 240px; text-align: right; }
  .person-name {
    font-size: 24px; letter-spacing: 1px; text-transform: uppercase;
    padding-bottom: 4px; border-bottom: 1px solid var(--ink);
  }
  .person-title { font-size: 13px; margin-top: 3px; }
  .contact-list {
    position: absolute; left: 360px; top: 232px; list-style: none;
    font-size: 13px; line-height: 20px;
  }
  .contact-list li { display: flex; align-items: center; gap: 12px; }
  .contact-list svg { width: 11px; height: 11px; fill: var(--ink); flex: none; }
  .base-band { position: absolute; left: 0; right: 0; bottom: 0; height: 16px; background: var(--grey-band); }
  /* Back */
  .card-back {
    top: 470px;
    background: linear-gradient(160deg, var(--charcoal) 0%, var(--black) 55%, var(--charcoal) 100%);
  }
  .back-frame {
    position: absolute; left: 120px; top: 62px; width: 360px; height: 236px;
    border: 14px solid var(--yellow); border-radius: 22px;
    display: flex; align-items: center; justify-content: center; gap: 14px;
  }
  .back-brand { font-size: 34px; color: var(--yellow); letter-spacing: 0.5px; text-align: center; line-height: 1.15; }
  .back-square { width: 22px; height: 22px; background: var(--yellow); flex: none; }
</style>
</head>
<body>
  <section class="card card-front" aria-label="Card front">
    <div class="front-brand"><span class="brand-square"></span>Wayline Billboard Co</div>
    <div class="divider"></div>
    <div class="company-block">
      <p class="company-name">Wayline Billboard Co</p>
      <p>PO Box 412, Harbourside NSW 2061</p>
    </div>
    <div class="person-block">
      <p class="person-name">Dale Thornton</p>
      <p class="person-title">Founder</p>
    </div>
    <ul class="contact-list">
      <li><svg viewBox="0 0 10 10"><rect x="2.5" y="0" width="5" height="10" rx="1"/></svg>+61 4 0312 5527</li>
      <li><svg viewBox="0 0 10 10"><path d="M5 0 L10 5 H8.5 V10 H1.5 V5 H0 Z"/></svg>1800WAYLINE</li>
      <li><svg viewBox="0 0 10 10"><path d="M0 2 H10 V8 H0 Z M0 2 L5 6 L10 2" stroke="#f3ec1f" stroke-width="0.8"/></svg>dale@wayline.com.au</li>
      <li><svg viewBox="0 0 10 10"><circle cx="5" cy="5" r="5"/></svg>www.wayline.com.au</li>
    </ul>
    <div class="base-band"></div>
  </section>

  <section class="card card-back" aria-label="Card back">
    <div class="back-frame">
      <span class="back-square"></span>
      <p class="back-brand">Wayline<br>Billboard Co</p>
    </div>
  </section>
</body>
</html>
```